Cardiology practice business card

We need a business card for our cardiology practice "Wattle Cardiology". We have a new logo, attached below. We like the colours in the logo - red and charcoal. The front of the business card will need to have the doctors name, address, phone number and email. The back will need to have space to write 2 appointment dates and times.

```html
<!DOCTYPE html>
<html lang="en">
<head>
<meta charset="utf-8">
<title>Wattle Cardiology – Business Card</title>
<link href="https://fonts.googleapis.com/css2?family=Montserrat:wght@400;500;600&display=swap" rel="stylesheet">
<style>
  :root {
    --red: #c0141c;
    --charcoal: #4a4a4c;
    --grey-text: #555;
    --line: #bdbdbd;
    --paper: #ffffff;
    --backdrop: #3b3b3d;
  }
  * { box-sizing: border-box; margin: 0; padding: 0; }
  html, body { width: 1200px; height: 689px; overflow: hidden; }
  body {
    background: var(--backdrop);
    font-family: "Montserrat", Arial, sans-serif;
    position: relative;
  }
  .card {
    position: absolute;
    top: 195px;
    width: 525px;
    height: 300px;
    background: var(--paper);
    border-radius: 18px;
    overflow: hidden;
  }
  .card--back { left: 45px; }
  .card--front { left: 630px; }

  .brand {
    position: absolute;
    display: flex;
    align-items: center;
    gap: 8px;
    color: var(--red);
    font-weight: 600;
    text-transform: uppercase;
    letter-spacing: 1px;
  }
  .brand__dot {
    width: 14px; height: 14px;
    border-radius: 50%;
    background: var(--red);
  }

  /* back: appointment side */
  .card--back .brand { left: 28px; top: 78px; font-size: 17px; }
  .appt-title {
    position: absolute;
    right: 40px; top: 34px;
    color: var(--red);
    font-size: 24px;
    font-weight: 500;
  }
  .appt-row {
    position: absolute;
    left: 28px; right: 28px;
    display: flex;
    align-items: flex-end;
    gap: 6px;
    color: var(--red);
    font-size: 14px;
  }
  .appt-row--first { top: 140px; }
  .appt-row--second { top: 182px; }
  .appt-row__fill {
    flex: 1;
    border-bottom: 1px dotted var(--charcoal);
    margin-bottom: 4px;
  }
  .appt-row__fill--date { flex: 1.3; }
  .appt-row__ampm { font-size: 12px; }
  .back-band {
    position: absolute;
    left: 0; right: 0; top: 222px;
    height: 24px;
    background: var(--red);
    color: #fff;
    font-size: 12px;
    letter-spacing: 2.5px;
    text-align: center;
    line-height: 24px;
  }
  .notice {
    position: absolute;
    left: 0; right: 0; top: 262px;
    text-align: center;
    color: var(--grey-text);
    font-size: 11.5px;
    letter-spacing: 0.4px;
  }

  /* front: contact side */
  .card--front .brand { right: 32px; top: 44px; font-size: 22px; }
  .divider {
    position: absolute;
    height: 1px;
    background: var(--line);
  }
  .divider--top { left: 190px; right: 30px; top: 108px; }
  .divider--name { left: 30px; width: 210px; top: 228px; }
  .address {
    position: absolute;
    right: 32px; top: 120px;
    text-align: right;
    color: var(--grey-text);
    font-size: 14px;
    line-height: 1.35;
  }
  .person-name {
    position: absolute;
    left: 30px; top: 196px;
    color: var(--red);
    font-size: 23px;
    font-weight: 600;
  }
  .contact {
    position: absolute;
    left: 30px; top: 234px;
    list-style: none;
    color: var(--grey-text);
    font-size: 13px;
    line-height: 1.45;
  }
  .contact li { display: flex; align-items: center; gap: 7px; }
  .contact svg { width: 11px; height: 11px; fill: var(--red); }
  .front-base {
    position: absolute;
    left: 0; bottom: 0;
    width: 525px; height: 62px;
  }
  .front-url {
    position: absolute;
    right: 28px; bottom: 22px;
    color: #fff;
    font-size: 13px;
    letter-spacing: 0.5px;
  }
</style>
</head>
<body>

<section class="card card--back" aria-label="Appointment card">
  <div class="brand"><span class="brand__dot"></span>Wattle Cardiology</div>
  <h2 class="appt-title">Next Appointment</h2>

  <div class="appt-row appt-row--first">
    <span>Date :</span><span class="appt-row__fill appt-row__fill--date"></span>
    <span>Time :</span><span class="appt-row__fill"></span>
    <span class="appt-row__ampm">AM/PM</span>
  </div>
  <div class="appt-row appt-row--second">
    <span>Date :</span><span class="appt-row__fill appt-row__fill--date"></span>
    <span>Time :</span><span class="appt-row__fill"></span>
    <span class="appt-row__ampm">AM/PM</span>
  </div>

  <div class="back-band">www.wattlecardio.com</div>
  <p class="notice">Please give 24 hours notice cancelling your appointment or a fee may be charged</p>
</section>

<section class="card card--front" aria-label="Contact card">
  <div class="brand"><span class="brand__dot"></span>Wattle Cardiology</div>
  <div class="divider divider--top"></div>
  <address class="address" style="font-style:normal">412 Juniper Road<br>Kelmont, Canada 48211</address>

  <h1 class="person-name">Daniel Hartley</h1>
  <div class="divider divider--name"></div>
  <ul class="contact">
    <li>
      <svg viewBox="0 0 24 24" aria-hidden="true"><path d="M6.6 10.8a15.5 15.5 0 0 0 6.6 6.6l2.2-2.2a1 1 0 0 1 1-.25 11.4 11.4 0 0 0 3.6.57 1 1 0 0 1 1 1V20a1 1 0 0 1-1 1A17 17 0 0 1 3 4a1 1 0 0 1 1-1h3.5a1 1 0 0 1 1 1c0 1.25.2 2.45.57 3.6a1 1 0 0 1-.25 1z"/></svg>
      555-014-2987
    </li>
    <li>
      <svg viewBox="0 0 24 24" aria-hidden="true"><path d="M2 5h20v14H2zM3.5 6.5 12 13l8.5-6.5z"/></svg>
      info@wattlecardio.com
    </li>
  </ul>

  <svg class="front-base" viewBox="0 0 525 62" aria-hidden="true">
    <defs>
      <linearGradient id="swoosh" x1="0" x2="1" y1="0" y2="0">
        <stop offset="0" stop-color="#2f2f31"/>
        <stop offset="0.6" stop-color="#8a8a8c"/>
        <stop offset="1" stop-color="#3c3c3e"/>
      </linearGradient>
    </defs>
    <path d="M0 44 L285 44 Q295 44 297 36 L300 22 Q302 14 312 14 L525 14 L525 62 L0 62 Z" fill="url(#swoosh)"/>
    <path d="M0 52 L290 52 Q300 52 302 44 L305 28 Q307 20 317 20 L525 20 L525 62 L0 62 Z" fill="var(--red)"/>
  </svg>
  <span class="front-url">www.wattlecardio.com</span>
</section>

</body>
</html>
```